Fence Flyer to Attract More Sales During Winter

We need a new flyer made that we can distribute to residential mailboxes. The flyer is to promote our Frostline Picket Days. We like simply designs, and we would like the flyer to showcase a lot of our fence photos. More of our photos are online at our website at www.getbramblerail.com - our new address needs to also be featured on the flyer - 436 Quillen rd, Monroe, NC 28117. I do want the words "FROSTLINE PICKET DAYS" to be dominate on the flyer with the description "Wood fences starting at $12/FT!" Please look through our Facebook page and our website to gather more photos or information. We are flexible on colors, nothing to fancy - simple flyer design please.

Target Market(s)

Residential homeowners that need a new fence to enclose their yard for safety, security or decorative

Industry/Entity Type

Residential Construction

Font styles to use
Sans Serif

Colors

Designer to choose colors to be used in the design.

Requirements
Must have
• Frostline Picket Days
• Contact information for the business
• "Come visit our outdoor showroom, open 24/7!"
Nice to have
• Photos of our fences - you can find more on our website at www.GetBrambleRail.com or Facebook.com/MeadowlarkRailGPV
Should not have
• Flashy designs

```html
<!DOCTYPE html>
<html lang="en">
<head>
<meta charset="utf-8">
<title>Frostline Picket Days Brochure</title>
<link href="https://fonts.googleapis.com/css2?family=Montserrat:wght@700;800&family=Open+Sans:wght@400;600;700&display=swap" rel="stylesheet">
<style>
  :root{
    --bg:#b9d0d1;
    --brown:#4a2d14;
    --tan:#c9a66b;
    --cream:#f4ead7;
    --white:#ffffff;
    --grey:#5d5d5d;
  }
  *{box-sizing:border-box;margin:0;padding:0}
  html,body{width:1200px;height:720px;overflow:hidden}
  body{background:var(--bg);font-family:"Open Sans",sans-serif;position:relative}
  .spread{position:absolute;left:30px;top:80px;width:1140px;height:560px;display:flex;box-shadow:0 10px 30px rgba(0,0,0,.2)}
  .panel{position:relative;width:380px;height:560px;background:var(--brown);overflow:hidden}
  .panel + .panel{border-left:1px solid rgba(0,0,0,.25)}
  .photo{position:absolute}
  .photo--worker{left:0;top:0;width:380px;height:270px;background:linear-gradient(135deg,#d9bf8f,#b8925d 55%,#7c6a55)}
  .photo--yard{left:0;top:472px;width:190px;height:88px;background:linear-gradient(160deg,#6f8f4a,#a8895b 60%,#7a5a34)}
  .cover-wedge{position:absolute;left:0;top:0;width:380px;height:560px}
  .cover-title{position:absolute;left:26px;top:192px;font-family:"Montserrat",sans-serif;font-weight:800;color:var(--white);font-size:27px;line-height:1.08;letter-spacing:1px;text-transform:uppercase}
  .price-band{position:absolute;left:0;top:300px;width:380px;height:44px;background:var(--tan);color:var(--white);font-weight:700;font-size:14px;letter-spacing:1px;text-transform:uppercase;line-height:1.3;padding:4px 20px}
  .showroom{position:absolute;left:20px;top:352px;width:210px;color:var(--cream);font-size:9.5px;line-height:1.45;text-transform:uppercase;font-weight:600}
  .call{position:absolute;left:20px;top:400px;display:flex;align-items:center;gap:10px;color:var(--white)}
  .call__label{font-weight:700;font-size:13px;letter-spacing:1px;line-height:1.2}
  .call__number{font-size:16px;letter-spacing:1px;line-height:1.2}
  .address{position:absolute;left:20px;top:446px;color:var(--cream);font-size:9.5px;font-weight:600;text-transform:uppercase;white-space:nowrap}
  .logo-box{position:absolute;left:200px;top:466px;width:170px;height:86px;background:var(--grey);padding:6px}
  .logo-box__inner{background:var(--white);width:100%;height:100%;display:flex;flex-direction:column;justify-content:center;padding:0 8px}
  .brand-name{font-weight:700;font-size:14px;color:var(--brown);display:flex;align-items:center;gap:6px;white-space:nowrap;line-height:1.2}
  .brand-mark{width:10px;height:10px;border-radius:50%;background:var(--tan);flex:none}
  .brand-phone{font-weight:700;font-size:13px;color:var(--brown);margin-top:2px;line-height:1.2}
  .brand-slogan{font-size:6.5px;color:var(--brown);margin-top:3px;white-space:nowrap}
  .top-strip{position:absolute;left:0;top:0;width:100%;height:16px;background:var(--tan)}
  .heading-tab{position:absolute;top:16px;left:50%;transform:translateX(-50%);background:var(--tan);color:var(--white);font-weight:700;font-size:20px;padding:4px 34px 6px;border-radius:0 0 4px 4px;white-space:nowrap}
  .about-text{position:absolute;left:26px;top:70px;width:328px;color:var(--cream);font-size:8.6px;line-height:1.6;text-transform:uppercase}
  .about-text p + p{margin-top:8px}
  .photo-pair{position:absolute;left:0;top:300px;width:380px;height:160px;background:var(--tan);display:flex;gap:8px;padding:8px}
  .photo-pair .shot{flex:1;position:relative}
  .shot--install{background:linear-gradient(150deg,#8fa86a,#b9976a 55%,#6e5233)}
  .shot--picket{background:linear-gradient(170deg,#9bb3c4,#e0c794 50%,#8e7a5a)}
  .footer-strip{position:absolute;left:0;bottom:0;width:100%;height:40px;background:var(--tan);color:var(--white);font-size:8.5px;font-weight:600;text-transform:uppercase;display:flex;align-items:center;justify-content:center;letter-spacing:.3px;white-space:nowrap}
  .tagline{position:absolute;left:0;top:92px;width:100%;text-align:center;color:var(--cream);font-size:19px;line-height:1.3}
  .service-grid{position:absolute;left:20px;top:180px;width:340px;display:flex;gap:14px}
  .service{flex:1}
  .service .shot{height:170px}
  .shot--aluminum{background:linear-gradient(160deg,#4f7a3a,#2c2c2c 55%,#6c9b4a)}
  .shot--wood{background:linear-gradient(160deg,#5d7e3f,#d2b27c 55%,#7fa65a)}
  .service__name{color:var(--cream);font-size:15px;text-align:center;margin-top:12px}
</style>
</head>
<body>
<main class="spread">

  <section class="panel panel--cover">
    <div class="photo photo--worker" role="img" aria-label="Installer nailing boards on a new wood privacy fence"></div>
    <svg class="cover-wedge" viewBox="0 0 380 560" aria-hidden="true">
      <polygon points="0,160 60,160 150,270 0,270" fill="var(--brown)"/>
      <polygon points="150,270 380,240 380,300 0,300 0,270" fill="var(--brown)"/>
      <polygon points="0,150 58,150 150,262 140,270 60,170 0,170" fill="var(--tan)"/>
    </svg>
    <h1 class="cover-title">Frostline<br>Picket<br>Days</h1>
    <div class="price-band">Wood fences<br>starting at $12/FT!</div>
    <p class="showroom">Outdoor showroom is open 24/7 on site estimates are available by appointment</p>
    <div class="call">
      <svg width="24" height="24" viewBox="0 0 24 24" aria-hidden="true"><path d="M6 3l3 0 2 5-2 1.5c1 2.5 3 4.5 5.5 5.5L16 13l5 2v3c0 1.5-1 2.5-2.5 2.5C10 20 4 14 3.5 5.5 3.5 4 4.5 3 6 3z" fill="var(--tan)"/></svg>
      <div>
        <div class="call__label">CALL US</div>
        <div class="call__number">704.555.0139</div>
      </div>
    </div>
    <p class="address">436 Quillen rd, Monroe, NC 28117</p>
    <div class="photo photo--yard" role="img" aria-label="Finished wood fence enclosing a green backyard"></div>
    <div class="logo-box">
      <div class="logo-box__inner">
        <div class="brand-name"><span class="brand-mark"></span>Meadowlark Rail</div>
        <div class="brand-phone">704-555-0139</div>
        <div class="brand-slogan">"Because Good Fences Make Good Neighbors"</div>
      </div>
    </div>
  </section>

  <section class="panel panel--about">
    <div class="top-strip"></div>
    <h2 class="heading-tab">About Us</h2>
    <div class="about-text">
      <p>Meadowlark Rail consists of a growing team of individuals with over 30 years of experience within the fencing industry. Each member of our staff is well-trained and knowledgeable within their own specialty. All of our installers take pride in the work completed. In our eyes, we are only as successful as the completion of your job - each job is important to us and we strive to give you the best installation experience possible.</p>
      <p>There are many benefits to contacting Meadowlark Rail for your outdoor living needs. We always provide free estimates, can assist with HOA approvals, and provide an outstanding warranty for all workmanship!</p>
    </div>
    <div class="photo-pair">
      <div class="shot shot--install" role="img" aria-label="Crew installing a wood fence beside a house"></div>
      <div class="shot shot--picket" role="img" aria-label="New wood picket fence along a front yard"></div>
    </div>
    <div class="footer-strip">Visit us www.getbramblerail.com or facebook.com/meadowlarkrailgpv</div>
  </section>

  <section class="panel panel--services">
    <div class="top-strip"></div>
    <h2 class="heading-tab">Our Services</h2>
    <p class="tagline">Explore different<br>styles to find the best for you</p>
    <div class="service-grid">
      <div class="service">
        <div class="shot shot--aluminum" role="img" aria-label="Black aluminum fence around a garden"></div>
        <div class="service__name">Aluminum Fences</div>
      </div>
      <div class="service">
        <div class="shot shot--wood" role="img" aria-label="Long wood fence along a lawn"></div>
        <div class="service__name">Wood Fences</div>
      </div>
    </div>
    <div class="footer-strip">Visit us www.getbramblerail.com or facebook.com/meadowlarkrailgpv</div>
  </section>

</main>
</body>
</html>
```